Handmade candle business in melbourne requiring assistance with designing classy labels

My business name is Wick and Willow.
I specialise in making handmade candles, i'm based in Melbourne.
My moto is "Delicately hand poured and infused by me...for you"
wickwillow@lumora.net
0428 716 902

I need some assistance with designing my labels for my glass candles
I really like earthy colours and nothing too bright, but I want it to look classy and elegant and something that stands out from other homemade candle businesses.
I have attached a sample of a design that appeals to me but open to suggestions.

Industry/Entity Type

Business

```html
<!DOCTYPE html>
<html lang="en">
<head>
<meta charset="utf-8">
<title>Wick and Willow – Candle Labels</title>
<link rel="stylesheet" href="https://fonts.googleapis.com/css2?family=Arimo&family=Roboto+Condensed&display=swap">
<style>
  :root {
    --paper: #ffffff;
    --name: #a2481c;
    --slogan: #9aa043;
    --line-1: #e8700c;
    --line-2: #b4561c;
    --line-3: #7c3a2a;
    --line-4: #5c2a44;
    --line-5: #3c1a5c;
    --ink: #000000;
  }
  * { margin: 0; padding: 0; box-sizing: border-box; }
  html, body { width: 1200px; height: 1000px; overflow: hidden; background: var(--paper); }
  .sheet { position: relative; width: 1200px; height: 1000px; }

  .label { position: absolute; width: 336px; height: 336px; }
  .label__ring { position: absolute; inset: 0; border-radius: 50%; }
  .label__face {
    position: absolute; left: 25px; top: 25px; width: 286px; height: 286px;
    border-radius: 50%; background: var(--paper);
  }
  .label__text {
    position: absolute; left: 0; right: 0; top: 48px;
    text-align: center; font-family: "Arimo", Arial, sans-serif;
  }
  .label__maker { font-size: 34px; line-height: 40px; color: var(--name); letter-spacing: -0.5px; }
  .label__brand { font-size: 32px; line-height: 40px; color: var(--slogan); letter-spacing: -0.5px; }
  .label__motto { font-size: 21px; line-height: 21px; margin-top: 2px; }
  .label__motto span { display: block; }
  .label__motto .m1 { color: var(--line-1); }
  .label__motto .m2 { color: var(--line-2); }
  .label__motto .m3 { color: var(--line-3); }
  .label__motto .m4 { color: var(--line-4); }
  .label__motto .m5 { color: var(--line-5); }
  .label__contact {
    display: flex; align-items: center; justify-content: center; gap: 5px;
    font-family: "Roboto Condensed", "Arial Narrow", sans-serif; color: var(--ink);
    font-size: 19px; line-height: 26px;
  }
  .label__contact--phone { font-family: "Arimo", Arial, sans-serif; font-size: 21px; }
  .label__contact svg { width: 20px; height: 14px; flex: none; }

  .pos-a { left: 19px;  top: 20px; }
  .pos-b { left: 419px; top: 20px; }
  .pos-c { left: 832px; top: 20px; }
  .pos-d { left: 19px;  top: 627px; }
  .pos-e { left: 419px; top: 627px; }
  .pos-f { left: 832px; top: 627px; }

  .ring-paint  { background: linear-gradient(135deg, #d9661e 0%, #9a8f3a 35%, #c9461c 65%, #7d5a2e 100%); }
  .ring-woven  { background: linear-gradient(90deg, #6b5a3a 0%, #c9431e 30%, #8f8a3e 55%, #b2351c 80%, #5e4e34 100%); }
  .ring-stripe { background: linear-gradient(180deg, #8c2f24 0%, #c9ae7a 30%, #a8a05a 50%, #8a2a22 75%, #b48a5a 100%); }
  .ring-rug    { background: linear-gradient(45deg, #8e4a24 0%, #d2532a 40%, #9c6a3a 70%, #c04426 100%); }
  .ring-fire   { background: radial-gradient(circle at 85% 20%, #fff4c8 0%, #f0a030 25%, #c9650e 60%, #7a2e08 100%); }
  .ring-canyon { background: linear-gradient(160deg, #b0502a 0%, #6e2412 40%, #c05a30 70%, #4e1a0e 100%); }
</style>
</head>
<body>
<div class="sheet">

  <svg width="0" height="0" style="position:absolute">
    <defs>
      <symbol id="icon-mail" viewBox="0 0 20 14">
        <rect x="0" y="0" width="20" height="14" fill="#000"/>
        <path d="M1 1 L10 8 L19 1" fill="none" stroke="#fff" stroke-width="1.4"/>
        <path d="M1 13 L7.5 6.5 M19 13 L12.5 6.5" stroke="#fff" stroke-width="1.2"/>
      </symbol>
      <symbol id="icon-phone" viewBox="0 0 20 14">
        <path d="M1 5 Q10 -1 19 5 L17 7 L14 5.5 L14 3.5 Q10 2.5 6 3.5 L6 5.5 L3 7 Z" fill="#000"/>
        <path d="M5 7 L7 5 L13 5 L15 7 L17 13 L3 13 Z" fill="#000"/>
        <circle cx="10" cy="9.5" r="2" fill="#fff"/>
      </symbol>
    </defs>
  </svg>

  <!-- label template repeated six times with different rims -->
  <div class="label pos-a">
    <div class="label__ring ring-paint" role="img" aria-label="Rim of orange and green painted artwork"></div>
    <div class="label__face"></div>
    <div class="label__text">
      <p class="label__maker">nora ellison</p>
      <p class="label__brand">“Wick and Willow”</p>
      <p class="label__motto"><span class="m1">Delicately hand poured</span><span class="m2">and infused by me...</span><span class="m3">for you specialise in</span><span class="m4">making handmade</span><span class="m5">candles</span></p>
      <p class="label__contact"><svg><use href="#icon-mail"/></svg>wickwillow@lumora.net</p>
      <p class="label__contact label__contact--phone"><svg><use href="#icon-phone"/></svg>0428 716 902</p>
    </div>
  </div>

  <div class="label pos-b">
    <div class="label__ring ring-woven" role="img" aria-label="Rim of woven vertical stripes in olive, red and brown"></div>
    <div class="label__face"></div>
    <div class="label__text">
      <p class="label__maker">nora ellison</p>
      <p class="label__brand">“Wick and Willow”</p>
      <p class="label__motto"><span class="m1">Delicately hand poured</span><span class="m2">and infused by me...</span><span class="m3">for you specialise in</span><span class="m4">making handmade</span><span class="m5">candles</span></p>
      <p class="label__contact"><svg><use href="#icon-mail"/></svg>wickwillow@lumora.net</p>
      <p class="label__contact label__contact--phone"><svg><use href="#icon-phone"/></svg>0428 716 902</p>
    </div>
  </div>

  <div class="label pos-c">
    <div class="label__ring ring-stripe" role="img" aria-label="Rim of horizontal fabric stripes in red, tan and olive"></div>
    <div class="label__face"></div>
    <div class="label__text">
      <p class="label__maker">nora ellison</p>
      <p class="label__brand">“Wick and Willow”</p>
      <p class="label__motto"><span class="m1">Delicately hand poured</span><span class="m2">and infused by me...</span><span class="m3">for you specialise in</span><span class="m4">making handmade</span><span class="m5">candles</span></p>
      <p class="label__contact"><svg><use href="#icon-mail"/></svg>wickwillow@lumora.net</p>
      <p class="label__contact label__contact--phone"><svg><use href="#icon-phone"/></svg>0428 716 902</p>
    </div>
  </div>

  <div class="label pos-d">
    <div class="label__ring ring-rug" role="img" aria-label="Rim of diagonal woven rug pattern in red and brown"></div>
    <div class="label__face"></div>
    <div class="label__text">
      <p class="label__maker">nora ellison</p>
      <p class="label__brand">“Wick and Willow”</p>
      <p class="label__motto"><span class="m1">Delicately hand poured</span><span class="m2">and infused by me...</span><span class="m3">for you specialise in</span><span class="m4">making handmade</span><span class="m5">candles</span></p>
      <p class="label__contact"><svg><use href="#icon-mail"/></svg>wickwillow@lumora.net</p>
      <p class="label__contact label__contact--phone"><svg><use href="#icon-phone"/></svg>0428 716 902</p>
    </div>
  </div>

  <div class="label pos-e">
    <div class="label__ring ring-fire" role="img" aria-label="Rim of glowing orange firelight"></div>
    <div class="label__face"></div>
    <div class="label__text">
      <p class="label__maker">nora ellison</p>
      <p class="label__brand">“Wick and Willow”</p>
      <p class="label__motto"><span class="m1">Delicately hand poured</span><span class="m2">and infused by me...</span><span class="m3">for you specialise in</span><span class="m4">making handmade</span><span class="m5">candles</span></p>
      <p class="label__contact"><svg><use href="#icon-mail"/></svg>wickwillow@lumora.net</p>
      <p class="label__contact label__contact--phone"><svg><use href="#icon-phone"/></svg>0428 716 902</p>
    </div>
  </div>

  <div class="label pos-f">
    <div class="label__ring ring-canyon" role="img" aria-label="Rim of red sandstone canyon photograph"></div>
    <div class="label__face"></div>
    <div class="label__text">
      <p class="label__maker">nora ellison</p>
      <p class="label__brand">“Wick and Willow”</p>
      <p class="label__motto"><span class="m1">Delicately hand poured</span><span class="m2">and infused by me...</span><span class="m3">for you specialise in</span><span class="m4">making handmade</span><span class="m5">candles</span></p>
      <p class="label__contact"><svg><use href="#icon-mail"/></svg>wickwillow@lumora.net</p>
      <p class="label__contact label__contact--phone"><svg><use href="#icon-phone"/></svg>0428 716 902</p>
    </div>
  </div>

</div>
</body>
</html>
```